VELMOR Website Design

We need a website designed for our company VELMOR. We are a luxury lifestyle club that will provide benefits and services for our members. The site should be clean & sleek, preferably using black and white (or darker colors). (example sites: brastelle.com, fovix.com)

Here is a link of a sample page I did using wix. (https://dunmerel7.pagebuildr.com/mysite) This can be used to get a general idea.

Target Market(s)

Upper Middle Class in the United States

Number of Pages Required

5+ page

Font styles to use
Sans Serif
Other font styles liked:
• Arial (or other similar fonts)

Requirements
Must have
• A clean design that is eye-catching and speaks to our company.
Nice to have
• Ideas for copy.

```html
<!DOCTYPE html>
<html lang="en">
<head>
<meta charset="utf-8">
<title>VELMOR — A Members Only Lifestyle Club</title>
<link href="https://fonts.googleapis.com/css2?family=Montserrat:wght@400;500;600;800&display=swap" rel="stylesheet">
<style>
  :root {
    --bg: #000000;
    --ink: #ffffff;
    --ink-soft: #d8d8d8;
    --ink-muted: #9a9a9a;
    --line: #4a4a4a;
    --accent: #4a8fe2;
    --field: #2a2a2a;
    --footer: #0d0d0d;
    --chip: #2e2e2e;
  }
  * { margin: 0; padding: 0; box-sizing: border-box; }
  html, body { width: 1200px; height: 2368px; overflow: hidden; background: var(--bg); }
  body { position: relative; font-family: "Montserrat", Arial, sans-serif; color: var(--ink); }
  .abs { position: absolute; }

  .hero-photo { left: 0; top: 0; width: 1200px; height: 860px;
    background: radial-gradient(ellipse 520px 640px at 420px 330px, #8a8a8a 0%, #4a4a4a 40%, #161616 75%, #000 100%),
                linear-gradient(180deg, #3a3a3a 0%, #000 100%); }
  .hero-fade { left: 0; top: 600px; width: 1200px; height: 260px; background: linear-gradient(180deg, rgba(0,0,0,0) 0%, #000 100%); }

  .brand { left: 66px; top: 42px; font-size: 22px; font-weight: 500; letter-spacing: 5px; }
  .nav { top: 48px; display: flex; gap: 0; font-size: 13px; letter-spacing: 1.6px; font-weight: 500; }
  .nav a { color: var(--ink); text-decoration: none; position: absolute; white-space: nowrap; }
  .sign-in { left: 1055px; top: 43px; width: 77px; height: 28px; background: #4d4d4d; font-size: 12px; letter-spacing: 0.5px;
    display: flex; align-items: center; justify-content: center; }

  .hero-title { left: 0; width: 1200px; top: 346px; text-align: center; font-size: 40px; font-weight: 500; letter-spacing: 8px; line-height: 46px; }
  .btn { background: var(--accent); color: var(--ink); display: flex; align-items: center; justify-content: center; }
  .hero-btn { left: 527px; top: 472px; width: 144px; height: 33px; font-size: 13px; letter-spacing: 1.5px; font-weight: 500; }

  .photo { display: block; }
  .photo-party { left: 248px; top: 774px; width: 366px; height: 262px; background: linear-gradient(160deg, #cfcfcf 0%, #7a7a7a 45%, #2c2c2c 100%); }
  .photo-jet { left: 628px; top: 1086px; width: 349px; height: 262px; background: linear-gradient(180deg, #b9b9b9 0%, #e2e2e2 45%, #6f6f6f 100%); }
  .photo-crowd { left: 248px; top: 1402px; width: 366px; height: 262px; background: radial-gradient(ellipse at 70% 30%, #d6d6d6 0%, #6a6a6a 40%, #1b1b1b 100%); }

  .frames { left: 0; top: 0; }
  .section-title { font-size: 22px; font-weight: 500; letter-spacing: 1.6px; white-space: nowrap; }
  .section-body { font-size: 12px; line-height: 16px; color: var(--ink-soft); width: 300px; }
  .section-body p + p { margin-top: 16px; }
  .read-more { font-size: 12.5px; color: var(--ink-soft); }

  .join-title { left: 0; width: 1200px; top: 1746px; text-align: center; font-size: 29px; font-weight: 800; line-height: 37px; }
  .join-btn { left: 504px; top: 1838px; width: 192px; height: 43px; font-size: 14px; font-weight: 500; }

  .news-band { left: 0; top: 1950px; width: 1200px; height: 237px;
    background: linear-gradient(90deg, #2b2b2b 0%, #141414 40%, #1c1c1c 70%, #333 100%); }
  .news-title { left: 0; width: 1200px; top: 2007px; text-align: center; font-size: 22px; font-weight: 500; letter-spacing: 2.5px; }
  .news-sub { left: 0; width: 1200px; top: 2045px; text-align: center; font-size: 14px; color: var(--ink-soft); }
  .news-field { left: 281px; top: 2081px; width: 469px; height: 43px; background: var(--field); color: var(--ink-muted);
    font-size: 13px; letter-spacing: 1px; padding-left: 22px; display: flex; align-items: center; }
  .news-btn { left: 750px; top: 2081px; width: 171px; height: 43px; font-size: 13px; font-weight: 600; letter-spacing: 1.5px; }

  .footer { left: 0; top: 2187px; width: 1200px; height: 181px; background: var(--footer); }
  .footer-brand { left: 170px; top: 2244px; font-size: 34px; font-weight: 400; letter-spacing: 8px; color: #b5b5b5; }
  .footer-meta { left: 458px; top: 2255px; font-size: 12.5px; color: var(--ink-muted); letter-spacing: 0.5px; }
  .footer-meta span { margin: 0 12px; }
  .social { left: 853px; top: 2250px; display: flex; gap: 13px; }
  .social span { width: 26px; height: 26px; border-radius: 50%; background: var(--chip); display: block; }
</style>
</head>
<body>
  <div class="abs hero-photo" role="img" aria-label="Couple walking with rolling luggage through a hotel lobby, black and white"></div>
  <div class="abs hero-fade"></div>

  <div class="abs brand">VELMOR</div>
  <nav class="abs nav" style="left:0">
    <a style="left:669px">HOME</a>
    <a style="left:742px">ABOUT</a>
    <a style="left:826px">SERVICES AND BENEFITS</a>
  </nav>
  <div class="abs sign-in">SIGN IN</div>

  <h1 class="abs hero-title">A MEMBERS ONLY<br>LIFESTYLE CLUB</h1>
  <div class="abs btn hero-btn">GET STARTED</div>

  <svg class="abs frames" width="1200" height="1720" aria-hidden="true">
    <g stroke="#4a4a4a" stroke-width="1.5" fill="none">
      <polyline points="872,777 977,777 977,1036 627,1036 627,1071"/>
      <polyline points="282,1090 248,1090 248,1353 614,1353 614,1396"/>
      <polyline points="872,1397 977,1397 977,1664 627,1664 627,1630"/>
    </g>
  </svg>

  <div class="abs photo photo-party" role="img" aria-label="Group of friends laughing together at a rooftop party"></div>
  <div class="abs section-title" style="left:657px;top:765px">ABOUT VELMOR</div>
  <div class="abs section-body" style="left:657px;top:816px">
    <p>VELMOR is a members only lifestyle club founded in order to bring the best services, experiences, and opportunities to our diverse community of members.</p>
    <p>Our members consist of creatives, athletes, artists, and other professionals.</p>
  </div>
  <div class="abs read-more" style="left:657px;top:970px">Read More</div>

  <div class="abs section-title" style="left:284px;top:1080px">BENEFITS AND SERVICES</div>
  <div class="abs section-body" style="left:284px;top:1132px;width:310px">
    <p>VELMOR membership provides you with amazing benefits and services.</p>
    <p>Members receive access to the best accountants, attorneys, real estate agents, private bankers/advisers and more. VELMOR members also receive access to private flight travel, premium luxury gym memberships, private social clubs, and private investment opportunities.</p>
  </div>
  <div class="abs read-more" style="left:284px;top:1304px">Read More</div>
  <div class="abs photo photo-jet" role="img" aria-label="Travellers stepping down from a private jet onto the runway"></div>

  <div class="abs photo photo-crowd" role="img" aria-label="Concert crowd with raised hands under stage lights"></div>
  <div class="abs section-title" style="left:657px;top:1384px">EXPERIENCES</div>
  <div class="abs section-body" style="left:657px;top:1434px">
    <p>VELMOR is a members only lifestyle club founded in order to bring the best services, experiences, and opportunities to our diverse community of members.</p>
    <p>Our members consist of creatives, athletes, artists, and other professionals.</p>
  </div>
  <div class="abs read-more" style="left:657px;top:1582px">Read More</div>

  <h2 class="abs join-title">Join us and experience a better<br>way to lifstyle in real life</h2>
  <div class="abs btn join-btn">Become an Investor</div>

  <div class="abs news-band" role="img" aria-label="Blurred business meeting with people at a table"></div>
  <h3 class="abs news-title">JOIN OURNEWSLETTERS NOW!</h3>
  <div class="abs news-sub">Subscribe to our newsletters now and stay up to date with new exclusive offers.</div>
  <div class="abs news-field">Write your email here</div>
  <div class="abs btn news-btn">SUBSCRIBE</div>

  <footer class="abs footer"></footer>
  <div class="abs footer-brand">VELMOR</div>
  <div class="abs footer-meta">© 2018 by Northlight Studio.<span>|</span>CONTACT US</div>
  <div class="abs social" aria-label="Social links">
    <span></span><span></span><span></span><span></span><span></span>
  </div>
</body>
</html>
```